Real Estate Sign 2

Our company is called Harwick Tolland Realty. We are a real estate development company. We need a sign that we are going to hang outside of our projects that says: Another project brought to you by Harwick Tolland Realty... For Sale....(213) 555-0847. At the very bottom is needs to say CaBRE# 04736291" We want the Harwick Tolland Realty to be sophisticated, fresh, simple. We do not have a logo so maybe one can be incorporated into the sign. Sign will be about 30"x24"

Industry/Entity Type

Real Estate

```html
<!DOCTYPE html>
<html lang="en">
<head>
<meta charset="utf-8">
<title>Harwick Tolland Realty – For Sale Sign</title>
<link rel="stylesheet" href="https://fonts.googleapis.com/css2?family=Jost:wght@400;500&family=Oswald:wght@700&display=swap">
<style>
  :root {
    --sign-charcoal: #222221;
    --brand-red: #c10e1b;
    --text-white: #ffffff;
    --skyline-grey: #9d9d9d;
    --skyline-grey-light: #a8a8a8;
  }
  html, body {
    margin: 0;
    padding: 0;
    width: 1200px;
    height: 960px;
    overflow: hidden;
    background: var(--sign-charcoal);
  }
  .sign {
    position: relative;
    width: 1200px;
    height: 960px;
    background: var(--sign-charcoal);
    color: var(--text-white);
    text-align: center;
    overflow: hidden;
  }
  .sign__intro {
    position: absolute;
    top: 26px;
    left: 0;
    width: 100%;
    margin: 0;
    font-family: "Jost", sans-serif;
    font-weight: 400;
    font-size: 54px;
    line-height: 1;
    letter-spacing: 3px;
    text-transform: uppercase;
    white-space: nowrap;
  }
  .brand-band {
    position: absolute;
    top: 122px;
    left: 0;
    width: 100%;
    height: 278px;
    background: var(--brand-red);
  }
  .brand-band__name {
    position: absolute;
    top: 13px;
    left: 0;
    width: 100%;
    margin: 0;
    font-family: "Oswald", sans-serif;
    font-weight: 700;
    font-size: 142px;
    line-height: 1;
    letter-spacing: 1px;
    text-transform: uppercase;
    white-space: nowrap;
  }
  .brand-band__descriptor {
    position: absolute;
    top: 174px;
    left: 0;
    width: 100%;
    margin: 0;
    font-family: "Jost", sans-serif;
    font-weight: 400;
    font-size: 72px;
    line-height: 1;
    letter-spacing: 14px;
    text-indent: 14px;
    text-transform: uppercase;
    white-space: nowrap;
  }
  .listing__status {
    position: absolute;
    top: 433px;
    left: 0;
    width: 100%;
    margin: 0;
    font-family: "Oswald", sans-serif;
    font-weight: 700;
    font-size: 148px;
    line-height: 1;
    letter-spacing: 1px;
    text-transform: uppercase;
    white-space: nowrap;
  }
  .listing__phone {
    position: absolute;
    top: 586px;
    left: 0;
    width: 100%;
    margin: 0;
    font-family: "Jost", sans-serif;
    font-weight: 400;
    font-size: 78px;
    line-height: 1;
    white-space: nowrap;
  }
  .listing__license {
    position: absolute;
    top: 692px;
    left: 0;
    width: 100%;
    margin: 0;
    font-family: "Jost", sans-serif;
    font-weight: 400;
    font-size: 24px;
    line-height: 1;
    letter-spacing: 2px;
    white-space: nowrap;
  }
  .skyline {
    position: absolute;
    left: 0;
    bottom: 0;
    width: 100%;
    height: 220px;
    background: linear-gradient(180deg, var(--skyline-grey-light) 0%, var(--skyline-grey) 100%);
  }
</style>
</head>
<body>
  <main class="sign">
    <p class="sign__intro">Another project brought to you by</p>

    <section class="brand-band">
      <h1 class="brand-band__name">Harwick Tolland</h1>
      <p class="brand-band__descriptor">Realty</p>
    </section>

    <h2 class="listing__status">For Sale</h2>
    <p class="listing__phone">(213) 555-0847</p>
    <p class="listing__license">CaBRE# 04736291</p>

    <div class="skyline" role="img" aria-label="Grey city skyline illustration of apartment towers and small houses"></div>
  </main>
</body>
</html>
```